Business Card Design For DJ Company

I'm rebranding my wedding and event dj company. I am looking for a modern, luxury, & fun design to match my new logo and website design. Please see attached logo and new webpage design. Colors should match. Design should flow with logo and website for recognition. I want to attract young adults. I plan on printing metallic finish cards so please keep hat in mind.

Target Market(s)

Millennials

Contact Information for Business Card

Name: Dario Velloza
Company: Coral Tide Fiesta DJ
Services: DJ – Photo Booth – Event Lighting – LED Robot

Website: www.coraltidefiestadj.example
Email: dario@coraltidefiestadj.example
Phone: (555)014-7392

Instagram: @ctfiestadj
Facebook: @ctfiestadj
Twitter - @ctfiestadj

Se Habla Español

Font styles to use
Serif
Sans Serif

Colors

Designer to choose colors to be used in the design.

Requirements
Nice to have
• Transparent Gradient background - Image related to weddings

```html
<!DOCTYPE html>
<html lang="en">
<head>
<meta charset="utf-8">
<title>Coral Tide Fiesta DJ — Business Card</title>
<link href="https://fonts.googleapis.com/css2?family=Michroma&family=Arimo:wght@400&display=swap" rel="stylesheet">
<style>
  :root {
    --backdrop: #1d1d1d;
    --card: #fbfbfa;
    --bronze: #a8652a;
    --copper: #d9862f;
    --orange: #f29322;
    --sky: #3aaee0;
    --shadow: rgba(0,0,0,.45);
  }
  * { box-sizing: border-box; margin: 0; padding: 0; }
  html, body {
    width: 1200px; height: 1200px; overflow: hidden;
    background: var(--backdrop);
  }
  .stage {
    width: 1200px; height: 1200px;
    display: flex; flex-direction: column; align-items: center; justify-content: center;
    gap: 36px;
  }
  .card {
    position: relative;
    width: 900px; height: 514px;
    background: var(--card);
    border-radius: 22px;
    box-shadow: 0 14px 30px var(--shadow);
  }
  /* Front */
  .card--front { display: flex; align-items: center; justify-content: center; }
  .brand {
    display: flex; align-items: center; gap: 16px;
    font-family: "Michroma", sans-serif;
    color: var(--orange);
    font-size: 30px; letter-spacing: 2px; text-transform: uppercase;
    white-space: nowrap;
  }
  .brand__dot {
    width: 26px; height: 26px; border-radius: 50%;
    background: var(--sky);
  }
  /* Back */
  .holder {
    position: absolute; left: 70px; top: 62px;
    font-family: "Michroma", sans-serif; font-size: 26px; letter-spacing: 1px;
    font-weight: 400;
    text-transform: uppercase; color: var(--bronze);
  }
  .holder__last { color: var(--copper); }
  .contact-list, .social-list {
    position: absolute; left: 70px; list-style: none;
    font-family: "Arimo", sans-serif; color: var(--copper);
    font-size: 20px;
  }
  .contact-list { top: 118px; }
  .social-list { bottom: 70px; }
  .contact-list li, .social-list li {
    display: flex; align-items: center; gap: 14px; line-height: 32px;
    white-space: nowrap;
  }
  .icon { width: 20px; height: 20px; flex: none; fill: none; stroke: var(--bronze); stroke-width: 1.8; }
  .social-mark { width: 14px; height: 14px; margin: 0 3px; border-radius: 50%; background: var(--bronze); flex: none; }
  .brand--back {
    position: absolute; right: 60px; top: 252px;
    font-size: 22px; color: var(--copper);
  }
  .brand--back .brand__dot { width: 20px; height: 20px; background: var(--copper); }
  .services {
    position: absolute; right: 60px; bottom: 58px; list-style: none;
    font-family: "Michroma", sans-serif; font-size: 17px; text-transform: uppercase;
    color: var(--copper); text-align: right;
  }
  .services li { display: flex; align-items: center; justify-content: flex-end; gap: 16px; line-height: 30px; }
  .services li::after {
    content: ""; width: 9px; height: 9px; border-radius: 50%; background: var(--orange);
  }
</style>
</head>
<body>
<main class="stage">
  <section class="card card--front">
    <div class="brand"><span class="brand__dot"></span>Coral Tide Fiesta DJ</div>
  </section>

  <section class="card card--back">
    <h1 class="holder">Dario <span class="holder__last">Velloza</span></h1>

    <ul class="contact-list">
      <li>
        <svg class="icon" viewBox="0 0 24 24"><path d="M6 3l3 1 1 5-2 1a11 11 0 0 0 6 6l1-2 5 1 1 3-2 3C11 21 3 13 3 5z"/></svg>
        (555)014-7392
      </li>
      <li>
        <svg class="icon" viewBox="0 0 24 24"><rect x="3" y="6" width="18" height="12"/><path d="M3 6l9 7 9-7"/></svg>
        dario@coraltidefiestadj.example
      </li>
      <li>
        <svg class="icon" viewBox="0 0 24 24"><circle cx="12" cy="12" r="9"/><ellipse cx="12" cy="12" rx="4" ry="9"/><path d="M3 12h18M5 7h14M5 17h14"/></svg>
        www.coraltidefiestadj.example
      </li>
    </ul>

    <ul class="social-list">
      <li><span class="social-mark"></span>@ctfiestadj</li>
      <li><span class="social-mark"></span>socialhub.example/ctfiestadj</li>
      <li><span class="social-mark"></span>@ctfiestadj</li>
    </ul>

    <div class="brand brand--back"><span class="brand__dot"></span>Coral Tide Fiesta DJ</div>

    <ul class="services">
      <li>DJ</li>
      <li>Photo Booth</li>
      <li>Event Lighting</li>
      <li>LED Robot</li>
    </ul>
  </section>
</main>
</body>
</html>
```